Maple Ridge business card design

Card needs to include the following text/items:
Company Logo
Tobin Marsh
Phone # - 555-318-7642
service@mapleridgelandscaping.example
Lawn & landscape maintenance services

```html
<!DOCTYPE html>
<html lang="en">
<head>
<meta charset="utf-8">
<title>Maple Ridge Business Card</title>
<link rel="stylesheet" href="https://fonts.googleapis.com/css2?family=Montserrat:wght@400;700&display=swap">
<style>
  :root {
    --forest: #0b1f13;
    --rust: #8c3418;
    --paper: #ffffff;
    --ink-light: #e9ece8;
    --leaf: #1f5a2e;
    --backdrop: #cfd0d2;
  }
  * { box-sizing: border-box; margin: 0; padding: 0; }
  html, body { width: 1200px; height: 921px; overflow: hidden; }
  body {
    background: var(--backdrop);
    font-family: "Montserrat", sans-serif;
    display: flex;
    flex-direction: column;
    align-items: center;
    justify-content: center;
    gap: 56px;
  }
  .card {
    position: relative;
    width: 640px;
    height: 366px;
    background: var(--forest);
    overflow: hidden;
    box-shadow: 0 10px 24px rgba(0,0,0,.22);
  }

  /* Front */
  .front__brand {
    position: absolute;
    left: 0; top: 0;
    width: 256px; height: 100%;
    background: var(--paper);
    display: flex;
    flex-direction: column;
    align-items: center;
    justify-content: center;
    gap: 16px;
  }
  .brand-mark {
    width: 92px; height: 92px;
    border-radius: 50%;
    background: var(--leaf);
  }
  .brand-name {
    font-weight: 700;
    font-size: 28px;
    color: var(--leaf);
    letter-spacing: .5px;
  }
  .name-band {
    position: absolute;
    left: 268px; top: 22px;
    width: 340px; height: 112px;
    background: var(--rust);
    color: var(--paper);
    padding: 24px 22px;
  }
  .name-band__name { font-weight: 700; font-size: 34px; line-height: 1; }
  .name-band__title { font-size: 14px; margin-top: 8px; opacity: .9; }
  .front__details {
    position: absolute;
    left: 290px; top: 158px;
    right: 24px;
    color: var(--ink-light);
  }
  .tagline { font-weight: 700; font-size: 17px; line-height: 1.3; color: var(--paper); margin-bottom: 22px; }
  .contact { list-style: none; }
  .contact li {
    display: flex;
    align-items: center;
    gap: 12px;
    font-size: 12.5px;
    margin-bottom: 14px;
  }
  .contact svg { width: 15px; height: 15px; flex: none; fill: var(--paper); }

  /* Back */
  .back__brand {
    position: absolute;
    left: 0; right: 0; top: 60px;
    display: flex;
    flex-direction: column;
    align-items: center;
    gap: 16px;
  }
  .back__brand .brand-mark { width: 120px; height: 120px; background: #2f7a3d; }
  .back__brand .brand-name { color: var(--paper); font-size: 34px; }
  .tag-band {
    position: absolute;
    left: 0; right: 0; bottom: 54px;
    height: 30px;
    background: var(--rust);
    color: var(--paper);
    font-weight: 700;
    font-size: 15px;
    display: flex;
    align-items: center;
    justify-content: center;
  }
</style>
</head>
<body>
  <section class="card card--front">
    <div class="front__brand">
      <div class="brand-mark"></div>
      <div class="brand-name">Maple Ridge</div>
    </div>
    <div class="name-band">
      <div class="name-band__name">Tobin Marsh</div>
      <div class="name-band__title">Manager</div>
    </div>
    <div class="front__details">
      <p class="tagline">Lawn &amp;<br>landscape maintenance services</p>
      <ul class="contact">
        <li>
          <svg viewBox="0 0 16 16" aria-hidden="true"><path d="M1 7.5 15 1 9 15 7.5 9z"/></svg>
          service@mapleridgelandscaping.example
        </li>
        <li>
          <svg viewBox="0 0 16 16" aria-hidden="true"><path d="M3.5 1.5 6 4 4.7 5.8a9 9 0 0 0 5.5 5.5L12 10l2.5 2.5-1.7 2A12 12 0 0 1 1.5 3.2z"/></svg>
          +1 555-318-7642
        </li>
        <li>
          <svg viewBox="0 0 16 16" aria-hidden="true"><path d="M8 1a7 7 0 1 0 0 14A7 7 0 0 0 8 1zm0 1.6c.8 0 1.8 1.8 2 4.6H6c.2-2.8 1.2-4.6 2-4.6zM4.4 7.2H2.7a5.4 5.4 0 0 1 3-4c-.7 1-1.2 2.4-1.3 4zm0 1.6c.1 1.6.6 3 1.3 4a5.4 5.4 0 0 1-3-4zm1.6 0h4c-.2 2.8-1.2 4.6-2 4.6s-1.8-1.8-2-4.6zm5.6 0h1.7a5.4 5.4 0 0 1-3 4c.7-1 1.2-2.4 1.3-4zm0-1.6c-.1-1.6-.6-3-1.3-4a5.4 5.4 0 0 1 3 4z"/></svg>
          www.mapleridgelandscaping.example
        </li>
      </ul>
    </div>
  </section>

  <section class="card card--back">
    <div class="back__brand">
      <div class="brand-mark"></div>
      <div class="brand-name">Maple Ridge</div>
    </div>
    <div class="tag-band">Lawn &amp; landscape maintenance services</div>
  </section>
</body>
</html>
```